Tech Company New PowerPoint Design Project

We are an IT Managed services, cloud and cyber security company https://www.korvanti.com.au/ Requesting proposals for a PowerPoint deck template that can be used by our sales team when pitching clients, our head office is located in Australa and we do have regional offices in NZ , USA , SRI LANKA and SINGAPORE. and also required to have a proposal/SOW template created too (not sure if this is something that we can include to this proposal) we may need a lot of things done in future but this is where i like to get started for now.. please let m eknow your thoughts and if you have any questions.
Target Market(s)
Enterprise
Industry/Entity Type
Information Technology

```html
<!DOCTYPE html>
<html lang="en">
<head>
<meta charset="utf-8">
<title>Korvanti – Presentation Template</title>
<link href="https://fonts.googleapis.com/css2?family=Dosis:wght@600;700&family=Quicksand:wght@500&family=Arimo:wght@400&display=swap" rel="stylesheet">
<style>
  :root {
    --brand-blue: #33c3f0;
    --brand-grey: #616163;
    --paper: #ffffff;
    --ink: #111111;
    --backdrop-light: #5c5c5c;
    --backdrop-dark: #0e0e0e;
  }
  * { margin: 0; padding: 0; box-sizing: border-box; }
  html, body { width: 1200px; height: 960px; overflow: hidden; }
  body {
    position: relative;
    background: radial-gradient(ellipse 70% 60% at 50% 50%, var(--backdrop-light), var(--backdrop-dark));
    font-family: "Arimo", Arial, sans-serif;
  }
  .slide-frame { position: absolute; width: 529px; height: 396px; overflow: hidden; }
  .slide-frame--cover    { left: 57px;  top: 83px; }
  .slide-frame--split    { left: 615px; top: 83px; }
  .slide-frame--columns  { left: 57px;  top: 514px; }
  .slide-frame--circles  { left: 615px; top: 516px; }

  .slide {
    position: relative; width: 661px; height: 495px;
    transform: scale(0.8); transform-origin: 0 0;
    background: var(--paper);
  }
  .slide-shapes { position: absolute; inset: 0; width: 661px; height: 495px; }
  .slide-shapes .blue { fill: var(--brand-blue); }
  .slide-shapes .grey { fill: var(--brand-grey); }

  .brand-name {
    position: absolute;
    font-family: "Quicksand", sans-serif; font-weight: 500;
    line-height: 1; letter-spacing: 2px;
  }
  .brand-name--hero { left: 0; width: 661px; top: 30px; text-align: center; font-size: 64px; color: var(--brand-blue); }
  .brand-name--footer { right: 40px; top: 448px; font-size: 46px; color: var(--paper); }

  .cover-photo {
    position: absolute; left: 0; top: 219px; width: 661px; height: 174px;
    background: linear-gradient(100deg, #c9b8a4 0%, #e9e4dc 30%, #b9c2c8 55%, #7b5450 75%, #d6d1c8 100%);
  }
  .site-url {
    position: absolute; right: 50px; top: 412px;
    font-family: "Dosis", sans-serif; font-weight: 700; font-size: 22px;
    color: var(--paper); letter-spacing: 0.5px;
  }

  .section-tab {
    position: absolute; left: 36px;
    font-family: "Dosis", sans-serif; font-weight: 700; font-size: 31px;
    color: var(--paper); line-height: 1;
  }
  .service-copy {
    position: absolute; left: 35px; width: 397px;
    font-size: 14.4px; line-height: 17.7px; color: var(--ink);
    text-align: justify; height: 124px; overflow: hidden;
  }
  .service-photo { position: absolute; left: 446px; width: 192px; height: 128px; }
  .service-photo--harbour { top: 105px; background: linear-gradient(180deg, #3f4a66 0%, #8b7a86 45%, #c88a55 62%, #27303f 100%); }
  .service-photo--headset { top: 275px; background: linear-gradient(120deg, #fbe6c4 0%, #d8c7b0 35%, #6d6a6b 60%, #b7bcc4 100%); }

  .column-heading {
    position: absolute; top: 52px; width: 222px;
    font-family: "Dosis", sans-serif; font-weight: 700; font-size: 31px;
    color: var(--brand-blue); text-align: center; line-height: 1;
  }
  .column-box {
    position: absolute; top: 96px; width: 222px; height: 301px;
    background: var(--brand-grey); border-radius: 12px;
    padding: 22px 14px 0;
    color: var(--paper); font-size: 14.4px; line-height: 17.6px; text-align: center;
  }
  .column--left  { left: 49px; }
  .column--right { left: 351px; }

  .info-circle {
    position: absolute; top: 197px; width: 196px; height: 196px;
    border-radius: 50%; background: var(--brand-blue);
    display: flex; align-items: center; justify-content: center;
    padding: 0 22px;
    color: var(--paper); font-size: 14.4px; line-height: 17.6px; text-align: center;
  }
  .info-circle--one   { left: 26px; }
  .info-circle--two   { left: 231px; }
  .info-circle--three { left: 435px; }
</style>
</head>
<body>

  <!-- Cover -->
  <div class="slide-frame slide-frame--cover">
    <section class="slide">
      <svg class="slide-shapes" viewBox="0 0 661 495" aria-hidden="true">
        <polygon class="grey" points="0,142 284,142 302,162 661,162 661,166 0,166"/>
        <rect class="blue" x="0" y="170" width="661" height="48"/>
        <polygon class="blue" points="0,393 661,393 661,453 370,453 333,408 0,408"/>
      </svg>
      <div class="brand-name brand-name--hero">korvanti</div>
      <div class="cover-photo" role="img" aria-label="Photo of a team of colleagues meeting around a laptop in a bright office"></div>
      <div class="site-url">www.korvanti.com.au</div>
    </section>
  </div>

  <!-- Services with photos -->
  <div class="slide-frame slide-frame--split">
    <section class="slide">
      <svg class="slide-shapes" viewBox="0 0 661 495" aria-hidden="true">
        <rect class="grey" x="0" y="0" width="661" height="22"/>
        <polygon class="blue" points="0,53 185,53 202,90 0,90"/>
        <polygon class="blue" points="0,246 185,246 202,283 0,283"/>
        <polygon class="blue" points="0,433 661,433 661,495 371,495 336,450 0,450"/>
      </svg>
      <h2 class="section-tab" style="top:58px">SERVICES</h2>
      <p class="service-copy" style="top:108px">Lorem Ipsum is simply dummy text of the printing and typesetting industry. Lorem Ipsum has been the industry's standard dummy text ever since the 1500s, when an unknown printer took a galley of type and scrambled it to make a type specimen book. It has survived not only five centuries, but also the leap into electronic typesetting, remaining essentially unchanged. It was popularised in the 1960s with the release of</p>
      <div class="service-photo service-photo--harbour" role="img" aria-label="Photo of a harbour bridge at dusk"></div>
      <h2 class="section-tab" style="top:251px">SERVICES</h2>
      <p class="service-copy" style="top:302px">Lorem Ipsum is simply dummy text of the printing and typesetting industry. Lorem Ipsum has been the industry's standard dummy text ever since the 1500s, when an unknown printer took a galley of type and scrambled it to make a type specimen book. It has survived not only five centuries, but also the leap into electronic typesetting, remaining essentially unchanged. It was popularised in the 1960s with the release of</p>
      <div class="service-photo service-photo--headset" role="img" aria-label="Photo of a support headset resting on a laptop keyboard"></div>
      <div class="brand-name brand-name--footer">korvanti</div>
    </section>
  </div>

  <!-- Two service columns -->
  <div class="slide-frame slide-frame--columns">
    <section class="slide">
      <svg class="slide-shapes" viewBox="0 0 661 495" aria-hidden="true">
        <rect class="grey" x="0" y="0" width="661" height="22"/>
        <polygon class="blue" points="0,435 661,435 661,495 370,495 333,450 0,450"/>
      </svg>
      <h2 class="column-heading column--left">SERVICES</h2>
      <div class="column-box column--left">Lorem Ipsum is simply dummy text of the printing and typesetting industry. Lorem Ipsum has been the industry's standard dummy text ever since the 1500s, when an unknown printer took a galley of type and scrambled it to make a type specimen book. It has survived not only five centuries, but also the leap into electronic typesetting, remaining essentially unchanged.</div>
      <h2 class="column-heading column--right">SERVICES</h2>
      <div class="column-box column--right">Lorem Ipsum is simply dummy text of the printing and typesetting industry. Lorem Ipsum has been the industry's standard dummy text ever since the 1500s, when an unknown printer took a galley of type and scrambled it to make a type specimen book. It has survived not only five centuries, but also the leap into electronic typesetting, remaining essentially unchanged.</div>
      <div class="brand-name brand-name--footer">korvanti</div>
    </section>
  </div>

  <!-- Three circles -->
  <div class="slide-frame slide-frame--circles">
    <section class="slide">
      <svg class="slide-shapes" viewBox="0 0 661 495" aria-hidden="true">
        <rect class="grey" x="0" y="0" width="661" height="22"/>
        <polygon class="blue" points="0,41 89,41 120,146 0,146"/>
        <polygon class="grey" points="109,41 661,41 661,146 139,146"/>
        <polygon class="blue" points="0,436 661,436 661,495 371,495 334,452 0,452"/>
      </svg>
      <div class="info-circle info-circle--one">Lorem Ipsum is simply dummy text of the printing and typesetting industry. Lorem Ipsum has been the industry's standard dummy text ever since the 1500s,</div>
      <div class="info-circle info-circle--two">Lorem Ipsum is simply dummy text of the printing and typesetting industry. Lorem Ipsum has been the industry's standard dummy text ever since the 1500s,</div>
      <div class="info-circle info-circle--three">Lorem Ipsum is simply dummy text of the printing and typesetting industry. Lorem Ipsum has been the industry's standard dummy text ever since the 1500s,</div>
      <div class="brand-name brand-name--footer">korvanti</div>
    </section>
  </div>

</body>
</html>
```